Automotive Brand Survey Online

Hi guys, we are looking for a freelancer who can design User Interface design (UI) for a survey-online website layout. <br/><br/>For the content, there are question, choices, back and next buttons - as if you are designing a survey website.<br/><br/>There are 5 main contents of the website consists of:<br/>1. Single-answer question<br/>2. Yes/No-answer question<br/>3. Net Promoter Score (NPS) or 1-5 scale question<br/>4. Open-end question<br/>5. Thank you page when finish survey<br/><br/>Here is the demo and more description<br/>https://preview.quorvane.site/survey/
Target Market(s)
Car Owner
Industry/Entity Type
Automotive
Number of Pages Required
1 page

```html
<!DOCTYPE html>
<html lang="en">
<head>
<meta charset="UTF-8">
<title>Kaizora Owner Survey</title>
<link href="https://fonts.googleapis.com/css2?family=Catamaran:wght@500;600;700;800&family=Open+Sans:wght@400;600&display=swap" rel="stylesheet">
<style>
  :root {
    --maroon: #7a1d2b;
    --maroon-light: #8a3440;
    --forest: #0c3a2c;
    --forest-light: #4c6156;
    --ink: #0f3b2e;
    --option: #555555;
    --radio: #6a6a6a;
    --card: #ffffff;
    --card-edge: #dcdcdc;
    --page-top: #e6e6e6;
    --page-bottom: #f4f4f4;
    --footer: #414141;
    --track: #efefef;
  }
  * { box-sizing: border-box; margin: 0; padding: 0; }
  html, body { width: 1146px; height: 1200px; overflow: hidden; }
  body {
    position: relative;
    font-family: "Open Sans", sans-serif;
    background: linear-gradient(to bottom, var(--page-top), var(--page-bottom) 60%);
  }
  .site-header {
    position: absolute; left: 0; top: 0; width: 1146px; height: 134px;
    background: #fff; box-shadow: 0 1px 3px rgba(0,0,0,0.08);
  }
  .brand {
    position: absolute; left: 62px; top: 44px;
    display: flex; align-items: center; gap: 10px;
    font-family: "Catamaran", sans-serif; font-weight: 700;
    font-size: 32px; color: var(--forest); letter-spacing: 0.5px;
  }
  .brand-dot { width: 26px; height: 26px; border-radius: 50%; background: var(--forest); }
  .progress { position: absolute; left: 694px; top: 38px; width: 412px; }
  .progress-labels {
    display: flex; justify-content: space-between; align-items: baseline;
    font-family: "Catamaran", sans-serif; font-weight: 700; color: var(--ink);
    font-size: 19px; padding: 0 8px 0 6px; line-height: 1;
  }
  .progress-labels .caption { font-size: 21px; }
  .progress-track {
    margin-top: 12px; height: 33px; border: 3px solid var(--forest);
    border-radius: 17px; padding: 5px; background: #fff;
  }
  .progress-inner { height: 100%; border-radius: 10px; background: var(--track); overflow: hidden; }
  .progress-fill { width: 58%; height: 100%; background: var(--forest); border-radius: 8px 0 0 8px; }
  .page-title {
    position: absolute; left: 0; width: 100%; top: 164px; text-align: center;
    font-family: "Catamaran", sans-serif; font-weight: 800; font-size: 40px;
    color: var(--maroon); letter-spacing: 1px; line-height: 1;
  }
  .question-card {
    position: absolute; left: 87px; width: 990px;
    background: var(--card); border: 1px solid var(--card-edge);
    box-shadow: 0 1px 2px rgba(0,0,0,0.05);
  }
  .question-text {
    position: absolute; left: 36px; top: 28px;
    font-family: "Catamaran", sans-serif; font-weight: 500; font-size: 21px;
    color: var(--ink); letter-spacing: 0.4px; line-height: 1.2;
  }
  .question-text b { font-weight: 800; margin-right: 10px; }
  .option {
    position: absolute; display: flex; align-items: center; gap: 11px;
    font-size: 17px; color: var(--option); line-height: 1;
  }
  .radio { width: 19px; height: 19px; border: 1.5px solid var(--radio); border-radius: 50%; background: #fff; }
  .col-a { left: 74px; } .col-b { left: 471px; }
  .row-a { top: 83px; } .row-b { top: 122px; }
  .actions { position: absolute; top: 1025px; left: 286px; display: flex; gap: 10px; }
  .btn {
    width: 287px; height: 63px; border-radius: 32px; border: none;
    display: flex; align-items: center; justify-content: center; gap: 8px;
    font-family: "Catamaran", sans-serif; font-weight: 800; font-size: 21px;
    letter-spacing: 1.5px; color: #fff;
  }
  .btn-back { background: linear-gradient(to right, var(--maroon-light), var(--maroon)); }
  .btn-next { background: linear-gradient(to right, var(--forest-light), var(--forest)); }
  .site-footer {
    position: absolute; left: 0; top: 1129px; width: 1146px; height: 71px;
    background: var(--footer); color: #fff; text-align: center;
    font-family: "Catamaran", sans-serif; font-weight: 500; font-size: 15px;
    letter-spacing: 0.3px; padding-top: 30px;
  }
</style>
</head>
<body>
  <header class="site-header">
    <div class="brand"><span class="brand-dot"></span>Kaizora</div>
    <div class="progress">
      <div class="progress-labels"><span>0%</span><span class="caption">Progress bar</span><span>100%</span></div>
      <div class="progress-track"><div class="progress-inner"><div class="progress-fill"></div></div></div>
    </div>
  </header>

  <h1 class="page-title">Questions</h1>

  <section class="question-card" style="top:244px;height:180px;">
    <p class="question-text"><b>Q:</b>Fusce tellus Sed metus augue convallis et vehicula ut pulvinar ?</p>
    <label class="option col-a row-a"><span class="radio"></span>Allamcorper nonummy nibh ligula</label>
    <label class="option col-b row-a"><span class="radio"></span>Lacus Ut velit enim vestibulum</label>
    <label class="option col-a row-b"><span class="radio"></span>Pulvinar metus eget consectetuer</label>
    <label class="option col-b row-b"><span class="radio"></span>Non fermentum nec hendrerit</label>
  </section>

  <section class="question-card" style="top:438px;height:180px;">
    <p class="question-text" style="top:32px;"><b>Q:</b>Integer orci tellus tristique vitae consequat nec porta vel lectus ?</p>
    <label class="option col-a row-a" style="top:80px;"><span class="radio"></span>Allamcorper nonummy nibh ligula</label>
    <label class="option col-b row-a" style="top:80px;"><span class="radio"></span>Lacus Ut velit enim vestibulum</label>
    <label class="option col-a row-b" style="top:119px;"><span class="radio"></span>Pulvinar metus eget consectetuer</label>
    <label class="option col-b row-b" style="top:119px;"><span class="radio"></span>Non fermentum nec hendrerit</label>
  </section>

  <section class="question-card" style="top:632px;height:179px;">
    <p class="question-text" style="left:29px;"><b>Q:</b>Nulla sit amet diam aliquam enim Proin dui lectus cursus ?</p>
    <label class="option col-a row-a"><span class="radio"></span>Allamcorper nonummy nibh ligula</label>
    <label class="option col-b row-a"><span class="radio"></span>Lacus Ut velit enim vestibulum</label>
    <label class="option col-a row-b"><span class="radio"></span>Pulvinar metus eget consectetuer</label>
    <label class="option col-b row-b"><span class="radio"></span>Non fermentum nec hendrerit</label>
  </section>

  <section class="question-card" style="top:830px;height:151px;left:88px;">
    <p class="question-text" style="top:20px;"><b>Q:</b>Eu mattis laoreet viverra sit amet quam ?</p>
    <label class="option col-a row-a" style="top:67px;"><span class="radio"></span>Allamcorper nonummy nibh ligula</label>
    <label class="option col-b row-a" style="top:67px;"><span class="radio"></span>Lacus Ut velit enim vestibulum</label>
    <label class="option col-a row-b" style="top:106px;"><span class="radio"></span>Pulvinar metus eget consectetuer</label>
    <label class="option col-b row-b" style="top:106px;"><span class="radio"></span>Non fermentum nec hendrerit</label>
  </section>

  <nav class="actions">
    <button class="btn btn-back">
      <svg width="16" height="18" viewBox="0 0 16 18"><path d="M13 2 L3 9 L13 16 Z" fill="none" stroke="#fff" stroke-width="2.5" stroke-linejoin="round"/></svg>
      BACK
    </button>
    <button class="btn btn-next">
      NEXT
      <svg width="16" height="18" viewBox="0 0 16 18"><path d="M3 2 L13 9 L3 16 Z" fill="none" stroke="#fff" stroke-width="2.5" stroke-linejoin="round"/></svg>
    </button>
  </nav>

  <footer class="site-footer">© 2020 Company Name | All Rights Reserved | Disclaimer</footer>
</body>
</html>
```